'We're just a little bit different' business cards for an IT Startup

We are an Information Technology Start-up focusing on providing IT strategy services to large midcap and enterprise organisations. We need to create business cards which reflect us personally and our brand. Quorvix.io is looking to differentiate itself in the market by providing IT strategy that reflects Information technology today.
We would like business cards that:
- Are just a little bit different, so people read them
- Reflect that Quorvix.Io is a modern disruptive technology company
- Reinforces our brand – strategy reinvented
- Provides information about us that is deeper and richer than just here’s my mobile and email address. We’d like the business card to be a snapshot of who we individually. It might be fav movie, book, sports, favourite beer, my family etc, fav quote etc

I have attached a document which has details about me to use on a sample business card and it also includes snapshots of our website. Also attached is our logo. If you need more information please ask

Industry/Entity Type

Information Technology

Contact Information for Business Card

See attached document, for my personal details to use as a sample

Requirements
Must have
• my details
• web site - url quorvix.io
• something a little bit different
Nice to have
• I'd like to see the design incorporate information about us that lets them see us as fellow human beings not just a work person
Should not have
• standard bland business cards

```html
<!DOCTYPE html>
<html lang="en">
<head>
<meta charset="utf-8">
<title>Quorvix.io business cards</title>
<link rel="stylesheet" href="https://fonts.googleapis.com/css2?family=Open+Sans:wght@400;600;700;800&family=Montserrat:wght@600;800&family=Questrial&family=Roboto+Condensed:ital,wght@0,400;0,700;1,700&display=swap">
<style>
  :root {
    --page: #e6e6e6;
    --card: #ffffff;
    --blue-light: #0b94cf;
    --blue-deep: #0670a6;
    --red: #e8322b;
    --grey: #808285;
    --grey-dark: #6d6e71;
  }
  * { margin: 0; padding: 0; box-sizing: border-box; }
  html, body { width: 1200px; height: 746px; overflow: hidden; }
  body { background: var(--page); position: relative; font-family: "Open Sans", sans-serif; }

  .card { position: absolute; background: var(--card); overflow: hidden; }
  .card svg.card-shape { position: absolute; inset: 0; }

  /* Front */
  .card-front { left: 118px; top: 85px; width: 567px; height: 347px; }
  .brand-name {
    position: absolute; left: 140px; top: 128px;
    color: #fff; font-family: "Open Sans", sans-serif; font-weight: 700;
    font-size: 78px; line-height: 1; letter-spacing: -2px;
  }
  .brand-tagline {
    position: absolute; left: 245px; top: 201px;
    color: #fff; font-size: 18px; font-weight: 400; white-space: nowrap;
  }
  .front-strap {
    position: absolute; left: 0; right: 0; top: 289px;
    text-align: center; color: var(--grey-dark);
    font-size: 12px; font-weight: 700;
  }

  /* Back */
  .card-back { left: 552px; top: 324px; width: 570px; height: 343px; }
  .coffee-art {
    position: absolute; left: 173px; top: 14px; width: 190px; height: 157px;
    border-radius: 8px 8px 60px 60px;
    background: radial-gradient(circle at 50% 55%, rgba(232,50,43,0.28), rgba(232,50,43,0.08));
  }
  .profile {
    position: absolute; left: 116px; top: 182px;
    font-family: "Roboto Condensed", sans-serif; white-space: nowrap;
  }
  .profile-line { display: flex; align-items: baseline; line-height: 1; }
  .name { font-family: "Montserrat", sans-serif; font-weight: 600; font-size: 26px; color: var(--grey); letter-spacing: 0.6px; }
  .role { font-family: "Montserrat", sans-serif; font-weight: 800; font-size: 28px; color: var(--red); }
  .phone { font-size: 29px; color: var(--red); }
  .passion { font-family: "Questrial", sans-serif; font-size: 28px; color: var(--grey); }
  .email { font-size: 19px; color: var(--red); }
  .motto { font-style: italic; font-weight: 700; font-size: 25px; color: var(--red); margin-left: 5px; }
  .trait { font-size: 18px; color: var(--grey); letter-spacing: -0.3px; }
  .web { font-family: "Open Sans", sans-serif; font-weight: 700; font-size: 21px; color: var(--red); margin-left: 4px; }
  .back-brand {
    position: absolute; left: 396px; top: 289px;
    font-family: "Open Sans", sans-serif; font-weight: 700; font-size: 13px; color: var(--blue-deep);
  }
</style>
</head>
<body>

<section class="card card-front" aria-label="Card front">
  <svg class="card-shape" width="567" height="347" viewBox="0 0 567 347">
    <defs>
      <radialGradient id="frontBlue" cx="50%" cy="45%" r="65%">
        <stop offset="0" style="stop-color:#0b94cf"/>
        <stop offset="1" style="stop-color:#0670a6"/>
      </radialGradient>
    </defs>
    <rect width="567" height="347" fill="url(#frontBlue)"/>
    <path d="M0,0 Q106,150 35,287 L0,287 Z" fill="#fff"/>
    <path d="M567,0 Q460,190 532,287 L567,287 Z" fill="#fff"/>
    <rect x="0" y="287" width="567" height="24" fill="#fff"/>
  </svg>
  <p class="brand-name">quorvix</p>
  <p class="brand-tagline">strategy re_invented</p>
  <p class="front-strap">modern disruptive technology company</p>
</section>

<section class="card card-back" aria-label="Card back">
  <svg class="card-shape" width="570" height="343" viewBox="0 0 570 343">
    <defs>
      <radialGradient id="backBlue" cx="50%" cy="50%" r="70%">
        <stop offset="0" style="stop-color:#0b94cf"/>
        <stop offset="1" style="stop-color:#0670a6"/>
      </radialGradient>
    </defs>
    <path d="M0,105 Q84,220 23,343 L0,343 Z" fill="url(#backBlue)"/>
    <path d="M553,0 Q455,170 570,343 L570,0 Z" fill="url(#backBlue)"/>
  </svg>
  <div class="coffee-art" role="img" aria-label="Hand-drawn red coffee cup with rising steam"></div>
  <div class="profile">
    <p class="profile-line"><span class="name">JOHN NAME</span><span class="role">manager</span></p>
    <p class="profile-line"><span class="phone">035550142</span><span class="passion">Coffee maniac</span></p>
    <p class="profile-line"><span class="email">email@quorvix.com</span><span class="motto">“NEVER GIVE UP”</span></p>
    <p class="profile-line"><span class="trait">neat and cool person</span><span class="web">www.quorvix.com</span></p>
  </div>
  <p class="back-brand">quorvix</p>
</section>

</body>
</html>
```